Shopfront Graphics , front,side doors, small wall and mall entry.

New graphics retail store opening.

We are looking for a contemporary store front graphic that screams, Graphics, colour and ATTENTION.

The Fascia is approximately 3m high x 5 metres wide. We envisage a lightbox along the top and graphics continuing across the glass below.

We then have the side wall and graphics approximately 2.5m x 10m, and then second floor with glass and concrete.

Can we try a theme that partially covers all walls ..window frames and glass...Not overdone, but similar to the area covered in my demo pic of another store...Not just limited to the paint splash...your ideas...concepts?
Updates

Just to save all graphicos time at the initial concept stage,

Can we just stick to the front signage and the successful designer can just continue theme on other windows..
ORRRRRR..if you really want to impress and you have time....as before do the lot!
Just looking for the THEME layout at first.

Thanks
DL

Please see new front windows...do not follow this designers image, please ignore. But please note the front door now on Right hand side of front. 

We do have an interesting angle now, I would like minimal graphics now. ZenoPrints on light box above glass...but do need some theme.

I will place on here some more printed samples from our logo.

Note we need the TV screens to be seen  but some nice pattern/design to hold all the windows together!!

Thanks Desmond

OK we seem to be going the wrong way with splashes now..Too much and starting to look TOO colourful and TOO messy...I have attached some images that I took off Pixelbarn that are more in keeping with what I am looking for. I will also send you a rough sketch of an interior plan or "LOOK". 

The inside of the store is being professionally designed..White on white.. I am thinking of introducing one vibrant stripe.
Hope this helps with the "FEEL".....

Target Market(s)

This shop is a high street location with a lot of pedestrians.
The store is being designed as a fun collaborative store with seating and computer stations where anyone can come in and design, Photobooks, full colour T shirts, posters, Photogifts such as Mugs, Mouse mats, Canvas fine art pictures....

General atmosphere is FUN, entertaing and based on consumers wandering in, a bit like the MAPLE HALL experience.

We also make commercial signage, vehicle wraps, acrylic signs, photocopy and print banners. Regular signshop products.

Industry/Entity Type

Retail

Font styles to use
Sans Serif

Colors
9bcb3b
e34197
33a6d7

Requirements
Must have
• Our logo.
Lets concentrate on the main front window and light box with logo....see new updated files.
ZenoPrints, as designed by artflock guys!!
Nice to have
• THe walls and windows should have a theme pattern, like the attached sign shop. I like that look with the full colour splash but we are very open to your ideas.
Should not have
• Pictures of CATS!

```html
<!DOCTYPE html>
<html lang="en">
<head>
<meta charset="utf-8">
<title>ZenoPrints – Backwall Banner</title>
<link rel="stylesheet" href="https://fonts.googleapis.com/css2?family=Montserrat:wght@600;700&display=swap">
<style>
  :root {
    --page: #eeeeee;
    --navy-deep: #0a2a66;
    --navy: #1447a0;
    --sky: #4f9ee6;
    --haze: #e8eef7;
    --ink: #151515;
    --lime: #9bcb3b;
    --magenta: #e34197;
    --cyan: #33a6d7;
    --wave-red: #e2233a;
    --wave-yellow: #f4d21d;
    --wave-violet: #7b3fc4;
  }
  * { margin: 0; padding: 0; box-sizing: border-box; }
  html, body {
    width: 1200px;
    height: 720px;
    overflow: hidden;
    background: var(--page);
  }
  .banner {
    position: absolute;
    left: 40px;
    top: 24px;
    width: 1120px;
    height: 672px;
    overflow: hidden;
    background:
      radial-gradient(ellipse 55% 48% at 52% 58%, var(--haze) 0%, #b9d4f1 30%, var(--sky) 55%, var(--navy) 80%, var(--navy-deep) 100%);
  }
  .hands-art {
    position: absolute;
    left: 200px;
    top: 120px;
    width: 760px;
    height: 360px;
    border-radius: 45% 45% 20% 20%;
    background: radial-gradient(ellipse at 50% 60%, rgba(80, 150, 225, 0.45) 0%, rgba(80, 150, 225, 0) 70%);
  }
  .wave-art {
    position: absolute;
    left: 0;
    bottom: 0;
    width: 1120px;
    height: 330px;
    background:
      linear-gradient(100deg,
        rgba(226, 35, 58, 0.55) 0%,
        rgba(244, 210, 29, 0.5) 22%,
        rgba(155, 203, 59, 0.5) 40%,
        rgba(51, 166, 215, 0.45) 58%,
        rgba(123, 63, 196, 0.5) 76%,
        rgba(227, 65, 151, 0.55) 100%);
    -webkit-mask-image: linear-gradient(to bottom, transparent 0%, #000 45%);
            mask-image: linear-gradient(to bottom, transparent 0%, #000 45%);
  }
  .brand {
    position: absolute;
    left: 300px;
    top: 250px;
    display: flex;
    align-items: center;
    gap: 22px;
  }
  .brand-square {
    width: 46px;
    height: 46px;
    background: var(--magenta);
  }
  .brand-name {
    font-family: "Montserrat", sans-serif;
    font-weight: 700;
    font-size: 112px;
    line-height: 1;
    letter-spacing: -2px;
    color: var(--ink);
  }
  .services {
    position: absolute;
    left: 0;
    top: 432px;
    width: 1120px;
    list-style: none;
    text-align: center;
    font-family: "Montserrat", sans-serif;
    font-weight: 600;
    font-size: 18px;
    line-height: 36px;
    color: var(--ink);
    text-transform: uppercase;
  }
  .services li:nth-child(1) { padding-left: 40px; }
  .services li:nth-child(2) { padding-left: 60px; }
</style>
</head>
<body>
  <main class="banner">
    <div class="hands-art" role="img" aria-label="Silhouettes of raised hands against a glowing blue sky with soft light spots"></div>
    <div class="wave-art" role="img" aria-label="Flowing rainbow-coloured wave lines sweeping across the lower banner"></div>

    <div class="brand">
      <span class="brand-square"></span>
      <h1 class="brand-name">ZenoPrints</h1>
    </div>

    <ul class="services">
      <li>Photobooks, full colour T shirts, posters</li>
      <li>Photogifts: mugs, mouse mats, canvas fine art pictures</li>
      <li>Commercial signage: vehicle wraps, acrylic signs, photocopy and print banners</li>
    </ul>
  </main>
</body>
</html>
```